Dynamic Lead Design (Partial WebPage)

To encourage visitors to our website to donate to our organization, we would like to replace the Dynamic Lead on our website with one that will evoke emotion from the viewer and motivate them to donate generously.

The deliverable should be a mockup of the design in context of the current website. See attached file for editable area. Fonts used in the mockup should be code-able in HTML/CSS.

The website
http://www.tumorhope.org

Please use this wireframe for reference:
http://app.wiredraftly.com/8b1c47d2e09f3a5561c7d4e0a2b9f8c3d7e61a04/7718264

Content:
[Image should evoke emotion from the viewer and motivate them to donate generously.]
Headline - “Give to HAVEN.”
Sub Headline - “Cancer patients find answers here. Your donation makes that possible.”
Call to action label - “Donate”

We love these examples:

Mt. Orwell Hearts and Sharing (http://www.hs.mtorwell.org/mtorwell/v/index.jsp?vgnextoid=7a5d21f0c3b9e4d8VgnVCM100000481726bdRCRD)
Kindly Wells (http://www.kindlywells.org/)

Design Size:
width: 971px
height: 300px

***see attached document for design area***

- Organization Background -

Our website receives over 40,000 unique visitors each month - mostly cancer patients and their family members seeking information about their disease. We would like to drive our visitors to donate to our nonprofit throughout late November and December (the majority of our donations from individuals come in during that time period).

We will be mailing an appeal letter to our database in mid-November. With this banner ad, we seek to complement that appeal. Some key messages from our appeal are:

- We focus on getting patients and their loved ones the best, most up-to-date information from trusted doctors who are leaders in cancer research – for free. We don’t sell a particular product or procedure. We simply arm them with the most current information so they can make the best decision for their own (or their loved one’s) care.

- What is the value of the support they or someone they know has received from our organization? Twenty-five dollars? One hundred dollars? One thousand? Can you even put an amount to it? Whatever it is, please consider making an end of year donation to this organization that has helped so many, comforted hundreds of thousands of patients and caretakers, and been there when needed.

- 2014 will be a year of growth. We just hired our first executive director. She is experienced in helping small nonprofits grow in size, revenue, and scope, and will undoubtedly bring a new level of energy to our work.

- In just a few months, we will hold two patient forums – first-of-its-kind programs for the organization. As we continue to grow, we will be able to offer more of these types of programs to more patients throughout the US.

Industry/Entity Type

Charity

Requirements
Must have
• - Must Adhere to existing website branding

```html
<!DOCTYPE html>
<html lang="en">
<head>
<meta charset="utf-8">
<title>HAVEN – Give to HAVEN</title>
<link rel="stylesheet" href="https://fonts.googleapis.com/css2?family=Arimo:wght@400;700&family=Montserrat:wght@300;400;500;600&display=swap">
<style>
:root{
  --mint:#6dcca4;
  --mint-soft:#dff3ea;
  --salmon:#f59d86;
  --salmon-deep:#ea7a62;
  --slate:#77787a;
  --taupe:#a39892;
  --green-link:#198a4a;
  --text:#3a3a3a;
  --muted:#6f6f6f;
  --rule:#dcdcdc;
  --brand-text:#9a8d86;
  --white:#fff;
}
*{box-sizing:border-box;margin:0;padding:0}
html,body{width:1047px;height:1200px;overflow:hidden;background:var(--white);font-family:"Arimo",Arial,sans-serif;color:var(--text)}
.page{position:relative;width:1047px;height:1200px}
.brand-dot{position:absolute;left:46px;top:38px;width:80px;height:80px;border-radius:50%;background:var(--salmon)}
.brand-name{position:absolute;left:230px;top:38px;font-family:"Montserrat",sans-serif;font-weight:600;font-size:14.5px;line-height:16.3px;color:var(--brand-text);width:110px}
.search{position:absolute;left:474px;top:44px}
.search-field{position:absolute;left:30px;top:19px;width:284px;height:24px;border:1px solid #b9b9b9;background:#fff;font-size:10px;color:#777;padding:5px 4px}
.search-btn{position:absolute;left:320px;top:18px;width:52px;height:26px;background:var(--mint-soft);border:1px solid #a9dcc5;font-size:11px;font-weight:700;color:#333;text-align:center;line-height:24px}
.search-x{position:absolute;left:378px;top:21px;font-size:13px;color:#888}
.nav{position:absolute;top:152px;left:45px;height:46px}
.tab{position:absolute;top:0;height:46px;background:var(--mint);color:#fff;font-family:"Montserrat",sans-serif;font-weight:500;letter-spacing:1.2px;font-size:14px;line-height:15px;text-align:center;display:flex;align-items:center;justify-content:center;white-space:nowrap}
.tab.tight{font-size:12.5px;letter-spacing:.8px}
.tab.profile{background:var(--slate)}
.tab.donate{background:var(--salmon)}
.donate-badge{position:absolute;left:958px;top:115px;width:58px;height:58px;border-radius:50%;background:var(--salmon)}
.donate-badge span{position:absolute;left:18px;top:14px;width:22px;height:22px;border-radius:50%;background:#fff}
.hero{position:absolute;left:45px;top:198px;width:970px;height:298px;background:linear-gradient(90deg,#6b5d53,#5a4d44 60%,#4f433b)}
.hero-photo{position:absolute;left:0;top:0;width:340px;height:298px;background:radial-gradient(ellipse at 45% 45%,#8a6a57 0,#6f5a4c 45%,transparent 75%)}
.hero-title{position:absolute;left:378px;top:30px;font-family:"Montserrat",sans-serif;font-weight:300;font-size:54px;color:#fff;letter-spacing:.5px}
.hero-sub{position:absolute;left:380px;top:108px;font-family:"Montserrat",sans-serif;font-weight:400;font-size:22px;line-height:32px;color:#f3efe9}
.hero-cta{position:absolute;left:385px;top:192px;width:142px;height:51px;border-radius:5px;background:linear-gradient(#f7a08b,var(--salmon-deep));border:1px solid #f7b6a6;font-family:"Montserrat",sans-serif;font-size:21px;color:#333;text-align:center;line-height:49px}
.edit{position:absolute;left:56px;top:516px;font-size:13px;font-weight:700;color:#555}
.posts{position:absolute;left:45px;top:576px;width:688px}
.posts-head{font-size:18px;font-weight:700;color:var(--muted)}
.share{position:absolute;left:474px;top:-12px;width:198px;height:18px;border:1px solid #e46;border-radius:2px;font-size:12px;color:#333;padding-left:76px;line-height:16px}
.share i{position:absolute;top:2px;width:12px;height:12px}
.post{border-bottom:1px solid var(--rule);padding:0 0 28px}
.post h2{font-size:17px;line-height:21px;font-weight:700;color:var(--green-link);width:680px}
.meta{font-size:14px;color:#444;margin:2px 0 24px;word-spacing:4px}
.meta b{color:#333;word-spacing:0}.meta em{font-style:normal;font-weight:700;color:var(--green-link);word-spacing:0}
.post p{font-size:15.5px;line-height:20px;color:#333;width:655px}
.post p a{color:var(--green-link);font-style:italic;font-size:14.5px}
.sidebar{position:absolute;left:758px;top:520px;width:243px}
.social{display:flex;gap:24px;padding-left:26px}
.social span{width:30px;height:30px;border-radius:5px}
.ask{margin-top:24px;height:45px;background:var(--salmon);color:#fff;font-family:"Montserrat",sans-serif;font-size:20px;letter-spacing:1px;line-height:45px;padding-left:106px}
.side-h{font-size:18px;font-weight:700;color:var(--muted);margin-top:26px}
.side-link{display:block;font-size:13px;line-height:15px;font-weight:700;color:var(--green-link);margin-top:7px}
.forums-btn{margin-top:13px;height:45px;background:var(--salmon);color:#fff;font-family:"Montserrat",sans-serif;font-size:17px;line-height:20px;text-align:center;letter-spacing:1px;padding-top:3px}
.faculty{position:relative;margin-top:18px;height:138px;width:243px;background:linear-gradient(135deg,#9c8f86,#c7b5a6 50%,#8d817a)}
.faculty-note{position:absolute;left:38px;top:35px;width:170px;height:62px;background:var(--mint-soft);font-family:"Montserrat",sans-serif;font-size:12px;line-height:15px;color:#e9846c;text-align:center;letter-spacing:.8px;padding-top:2px}
.faculty-note b{color:#333;font-style:italic;font-size:11px;letter-spacing:0}
.cats{margin-top:26px}
.cat{height:22px;margin-bottom:2px;background:var(--taupe);color:#fff;font-family:"Montserrat",sans-serif;font-size:14.5px;text-align:center;line-height:22px}
</style>
</head>
<body>
<div class="page">
  <div class="brand-dot"></div>
  <div class="brand-name">Helping Access Vital Education Now</div>

  <div class="search">
    <svg width="406" height="64" viewBox="0 0 406 64"><path d="M24 3h358a21 21 0 0 1 21 21v14a21 21 0 0 1-21 21H24a21 21 0 0 1-21-21V24A21 21 0 0 1 24 3z" fill="#fff" stroke="#c8ead9" stroke-width="5"/><path d="M10 50 4 62 22 57" fill="#fff" stroke="#c8ead9" stroke-width="4"/></svg>
    <div class="search-field">Site Search</div>
    <div class="search-btn">Search</div>
    <div class="search-x">✕</div>
  </div>

  <div class="donate-badge"><span></span></div>
  <nav class="nav">
    <div class="tab" style="left:0;width:168px">ABOUT HAVEN</div>
    <div class="tab tight" style="left:170px;width:171px">ASK US<br>DISCUSSION FORUMS</div>
    <div class="tab" style="left:343px;width:170px">GENERAL<br>CANCER INFO</div>
    <div class="tab" style="left:516px;width:170px">FOCUSED<br>CANCER INFO</div>
    <div class="tab profile" style="left:689px;width:139px">PROFILE</div>
    <div class="tab donate" style="left:831px;width:139px">DONATE</div>
  </nav>

  <section class="hero">
    <div class="hero-photo" role="img" aria-label="Portrait photo of a young cancer patient looking at the viewer"></div>
    <h1 class="hero-title">Give to HAVEN</h1>
    <p class="hero-sub">Cancer patients find answers here.<br>Your donation makes that possible.</p>
    <div class="hero-cta">Donate</div>
  </section>

  <div class="edit">Edit</div>

  <main class="posts">
    <div class="share"><i style="left:4px;background:#3b5b98"></i><i style="left:18px;background:#4fb6e6"></i><i style="left:32px;background:#333"></i><i style="left:46px;background:#2a6fb7;border-radius:50%"></i>Share/Email/More</div>
    <div class="posts-head">Recent HAVEN News &amp; Posts</div>
    <article class="post" style="margin-top:47px">
      <h2>Cancer Care In Crisis? The Institute of Clinical Policy's Report: Delivering High-Quality Cancer Care: Charting a New Course For a System in Crisis; Part I: The Current Landscape</h2>
      <div class="meta">by <b>Dr. Lorne</b> on Nov 10, 2013 in <em>HAVEN :: Cancer Basics</em></div>
      <p>&nbsp;A few months ago, the Institute of Clinical Policy released the prepublication proofs of a massive report on the state of oncology care, saying that it was in crisis in the United States. I learned about it from an email that focused on the crisis part of the title. I was bo... <a>(Read More)</a></p>
    </article>
    <article class="post" style="margin-top:26px">
      <h2>Is there a place for live educational meetings in our new online world? Would you want to come?</h2>
      <div class="meta">by <b>Dr Hale</b> on Nov 8, 2013 in <em>HAVEN :: Lung Cancer</em></div>
      <p>Back in 2009, HAVEN did a live educational meeting in Seattle, geared toward patients and caregivers, that coincided with a lung cancer conference offered to physicians. It included brief (~15 minute) talks by about 10 different specialists, ranging in topics from initi... <a>(Read More)</a></p>
    </article>
    <article class="post" style="margin-top:26px">
      <h2>Chat Thursday: The Tissue is the Issue, Key Challenges in Biopsies and Tissue Collection</h2>
      <div class="meta">by <b>Dr Hale</b> on Nov 5, 2013 in <em>HAVEN :: Lung Cancer</em></div>
      <p>This Thursday, November 7th at 8 PM Eastern, 5 PM Pacific, we'll gather in the Chirpverse for another one hour #TCXT (thoracic cancer exchange) chat. This time, the topic will be on biopsies and tissue collection. &nbsp;Now that we've entered a new era where more an... <a>(Read More)</a></p>
    </article>
  </main>

  <aside class="sidebar">
    <div class="social"><span style="background:#3b5b98"></span><span style="background:#4fb6e6"></span><span style="background:#c4302b"></span><span style="background:#f0812b"></span></div>
    <div class="ask">Ask Us</div>
    <div class="side-h">Welcome To HAVEN!</div>
    <a class="side-link">How To Use HAVEN</a>
    <a class="side-link">General Cancer FAQs</a>
    <a class="side-link" style="margin-top:12px">Recent HAVEN Site Post Comments</a>
    <div class="forums-btn">HAVEN<br>Discussion Forums</div>
    <a class="side-link" style="margin-top:12px">HAVEN Discussion Forum Guidelines</a>
    <a class="side-link" style="margin-top:12px">Recent HAVEN Forum Activity</a>
    <a class="side-link" style="margin-top:12px">Original HAVEN Archived Forums</a>
    <div class="faculty" role="img" aria-label="Grid of faculty member portrait photos">
      <div class="faculty-note">HAVEN is eager to bring in more great faculty members... <b>Interested? Click Here!</b></div>
    </div>
    <div class="cats">
      <div class="cat">Lung/Thoracic Cancer Info</div>
      <div class="cat">Breast Cancer Info</div>
      <div class="cat">Pancreatic Cancer Info</div>
      <div class="cat">Kidney Cancer Info</div>
      <div class="cat">Bladder Cancer Info</div>
      <div class="cat">Head/Neck Cancer Info</div>
    </div>
  </aside>
</div>
</body>
</html>
```